Business card with logo for a family psychologist

I need a business card for my private practice in the urban Chicago area as a psychologist. I see families and individuals who are going through difficult times - divorce, separation, illness, or trauma. I want to project hopefulness, competence, and caring.

Target Market(s)

Adults, other professionals - such as physicans and lawyers

Industry/Entity Type

Health Care

Contact Information for Business Card

Front should have my name and credentials; back should have location information including my email, phone

Font styles to use
Serif
Decorative
Script

Requirements
Must have
• Unique logo
Should not have
• No pictures or icons of people; no black

```html
<!DOCTYPE html>
<html lang="en">
<head>
<meta charset="utf-8">
<title>Dr. Dana Morrow – Business Card</title>
<link rel="stylesheet" href="https://fonts.googleapis.com/css2?family=Jost:wght@400&family=Cinzel:wght@400&family=Source+Sans+3:wght@400;600&display=swap">
<style>
  :root {
    --page: #e9e7e3;
    --card-front: #f3f3f3;
    --card-back: #ffffff;
    --blue: #2a87cc;
    --blue-deep: #1d6aab;
    --green: #8cc04b;
    --ink: #4b4b4b;
    --rule: #3a3a3a;
  }
  * { box-sizing: border-box; margin: 0; padding: 0; }
  html, body { width: 1200px; height: 900px; overflow: hidden; }
  body { background: var(--page); position: relative; font-family: "Source Sans 3", sans-serif; }

  .card {
    position: absolute;
    width: 600px;
    height: 343px;
    box-shadow: 0 6px 18px rgba(0,0,0,0.18);
    overflow: hidden;
  }

  /* Name side */
  .card--front { left: 500px; top: 70px; background: var(--card-front); }
  .front-mark {
    position: absolute; left: 150px; top: 128px;
    width: 46px; height: 46px; background: var(--blue);
  }
  .front-divider {
    position: absolute; left: 222px; top: 110px;
    width: 2px; height: 86px; background: var(--rule);
  }
  .front-name {
    position: absolute; left: 238px; top: 132px;
    font-family: "Jost", sans-serif; font-size: 36px; color: var(--ink);
    letter-spacing: 0.5px; line-height: 1;
  }
  .front-title {
    position: absolute; left: 240px; top: 178px;
    font-family: "Cinzel", serif; font-size: 13px; color: var(--ink);
    letter-spacing: 1px;
  }

  /* Contact side */
  .card--back { left: 100px; top: 470px; background: var(--card-back); }
  .back-shapes { position: absolute; inset: 0; }
  .back-name {
    position: absolute; left: 62px; top: 22px;
    font-weight: 600; font-size: 19px; color: var(--blue);
  }
  .back-title {
    position: absolute; left: 62px; top: 46px;
    font-size: 16px; color: var(--ink);
  }
  .address {
    position: absolute; left: 44px; top: 146px;
    font-size: 16px; line-height: 20px; color: var(--ink);
  }
  .contact-list { position: absolute; left: 28px; top: 192px; list-style: none; }
  .contact-list li {
    display: flex; align-items: center; gap: 6px;
    font-size: 16px; line-height: 21px; color: var(--ink);
  }
  .contact-list svg { width: 11px; height: 11px; flex: none; }
  .back-brand {
    position: absolute; left: 370px; top: 150px;
    display: flex; align-items: center; gap: 12px;
  }
  .back-brand__square { width: 30px; height: 30px; background: var(--green); }
  .back-brand__name {
    font-family: "Source Sans 3", sans-serif; font-weight: 600;
    font-size: 30px; color: var(--blue);
  }
</style>
</head>
<body>

<section class="card card--front" aria-label="Card front">
  <div class="front-mark"></div>
  <div class="front-divider"></div>
  <h1 class="front-name">Dr.Dana Morrow</h1>
  <p class="front-title">Licensed Clinical Psychologist</p>
</section>

<section class="card card--back" aria-label="Card back">
  <svg class="back-shapes" viewBox="0 0 600 343" width="600" height="343" aria-hidden="true">
    <defs>
      <linearGradient id="blueBand" x1="0" y1="0" x2="0" y2="1">
        <stop offset="0" stop-color="#3596d8"/>
        <stop offset="1" stop-color="#1d6aab"/>
      </linearGradient>
    </defs>
    <polygon points="0,40 20,22 40,22 20,40" fill="var(--green)"/>
    <polygon points="22,42 48,12 52,12 52,42" fill="url(#blueBand)"/>
    <polygon points="0,244 240,264 280,290 0,270" fill="var(--green)"/>
    <polygon points="300,292 600,318 600,343 285,343" fill="url(#blueBand)"/>
  </svg>

  <h2 class="back-name">Dana Morrow, Ph.D.</h2>
  <p class="back-title">Licensed Clinical Psychologist</p>

  <address class="address">
    250 W. Lakeview Suite 310<br>
    Chicago, Illinois 60610
  </address>

  <ul class="contact-list">
    <li>
      <svg viewBox="0 0 12 12"><path d="M3 1 L5 3.5 L4 5 Q5 7 7 8 L8.5 7 L11 9 L9.5 11 Q4 10.5 1 3 Z" fill="var(--blue)"/></svg>
      312-555-0148
    </li>
    <li>
      <svg viewBox="0 0 12 12"><rect x="0.5" y="2" width="11" height="8" fill="var(--blue)"/><path d="M0.5 2 L6 6.5 L11.5 2" stroke="#fff" stroke-width="1" fill="none"/></svg>
      drdanamorrow@example.com
    </li>
  </ul>

  <div class="back-brand">
    <span class="back-brand__square"></span>
    <span class="back-brand__name">Dana Morrow</span>
  </div>
</section>

</body>
</html>
```